Historic Church website

We want our church website to feel warm, historic, and clean, modern, and easy to navigate. Dont use the anchor

Current website: https://www.meadowlarkfellowship.org/

Requirements
Should not have
• I would like to use the logo without the anchor

```html
<!DOCTYPE html>
<html lang="en">
<head>
<meta charset="utf-8">
<title>Meadowlark Fellowship</title>
<link href="https://fonts.googleapis.com/css2?family=Cinzel:wght@400&family=Jost:wght@300;400&display=swap" rel="stylesheet">
<style>
:root{
  --bg:#141312;
  --bg-soft:#1b1a19;
  --card:#222120;
  --tan:#b88b66;
  --tan-light:#d9b48e;
  --gold:#c9a27a;
  --text:#f1ece6;
  --muted:#8f8a85;
  --line:#3a3836;
}
*{box-sizing:border-box;margin:0;padding:0}
html,body{width:1200px;height:4013px;overflow:hidden;background:var(--bg)}
body{position:relative;font-family:'Jost',sans-serif;font-weight:300;color:var(--text)}
.abs{position:absolute}
.gold{color:var(--gold)}
a{color:inherit;text-decoration:none}

/* hero */
.hero{left:0;top:0;width:1200px;height:541px;background:linear-gradient(180deg,#2b2520 0%,#4a3c31 40%,#3a2f27 75%,#1a1614 100%)}
.nav{top:54px;font-size:11px;letter-spacing:.5px;text-transform:uppercase}
.nav span{position:absolute;white-space:nowrap}
.brand{left:480px;top:38px;width:240px;text-align:center;font-weight:400;font-size:19px;letter-spacing:3px;line-height:1.4}
.brand small{display:block;font-size:9px;letter-spacing:4px;margin-top:6px}
.hero-title{top:232px;width:1200px;text-align:center;font-family:'Cinzel',serif;font-weight:400;font-size:44px;line-height:60px;letter-spacing:1px}
.watch{left:508px;top:387px;display:flex;align-items:center;gap:14px;font-size:13px;text-transform:uppercase}
.watch .play{width:46px;height:46px;border:1.5px solid var(--text);border-radius:50%}
.watch .rule{position:absolute;left:60px;top:36px;width:130px;height:1px;background:var(--text)}
.rail{left:60px;top:60px;width:1px;height:560px;background:rgba(255,255,255,.3)}
.dot{left:50px;width:22px;height:22px;border:1px solid rgba(255,255,255,.35);border-radius:50%;font-size:8px;text-align:center;line-height:20px;color:rgba(255,255,255,.6)}
.scroll{left:18px;top:540px;width:86px;height:86px;border:7px solid rgba(255,255,255,.35);border-radius:50%;font-size:8px;text-align:center;padding-top:24px;text-transform:uppercase}

/* about */
.about-photo{left:240px;top:541px;width:360px;height:479px;background:linear-gradient(170deg,#9fb7d4 0%,#e9e3da 35%,#d7cfc4 70%,#4a4538 100%)}
.vertical{left:160px;top:1020px;transform-origin:0 0;transform:rotate(-90deg);font-size:60px;font-weight:300;color:#2c2b2a;white-space:nowrap;letter-spacing:2px}
.about-head{left:661px;top:600px;width:420px;font-size:24px;line-height:31px;font-weight:400}
.about-text{left:661px;top:720px;width:430px;font-size:11.5px;line-height:18.2px;color:#c4beb8}
.btn-outline{left:661px;top:978px;width:131px;height:36px;border:1px solid var(--gold);font-size:11px;text-transform:uppercase;text-align:center;line-height:34px}
.pillar{top:1108px;display:flex;gap:14px}
.pillar h3{font-weight:400;font-size:16px;margin-bottom:8px}
.pillar p{font-size:11.5px;line-height:17px;color:#c4beb8;width:210px}

/* ministries */
.min-hall{left:620px;top:1304px;width:580px;height:480px;background:linear-gradient(160deg,#3a2818 0%,#6b4a2b 40%,#2a1d13 100%)}
.min-left{left:0;top:1394px;width:620px;height:390px;background:linear-gradient(120deg,#2a1f16 0%,#5a4330 50%,#332519 100%)}
.min-box{left:59px;top:1455px;width:502px;height:401px;background:var(--tan);padding:62px 62px 0}
.min-box h2{font-weight:300;font-size:25px;line-height:31px;color:#f6eee6;margin-bottom:30px}
.min-box li{list-style:none;font-size:11.5px;color:#f0e4d8;height:48px;line-height:48px;border-bottom:1px solid rgba(255,255,255,.25);display:flex;justify-content:space-between}
.min-box li:last-child{border-bottom:0}
.min-label{right:47px;top:1650px;text-align:right;font-size:58px;line-height:60px;color:rgba(255,255,255,.45);font-weight:300}

/* visit */
.sec-title{width:1200px;text-align:center;font-size:24px;font-weight:400}
.visit{left:210px;top:2022px;width:779px;height:273px}
.visit .vl{position:absolute;top:0;width:1px;height:273px;background:var(--line)}
.svc{position:absolute;text-align:center}
.svc h3{font-weight:400;font-size:22px;margin-bottom:14px}
.svc .time{font-size:12px;margin-bottom:12px}
.svc p{font-size:11px;line-height:18px;color:var(--muted)}

/* events */
.ev{top:2463px;width:257px;height:298px;background:var(--bg-soft);text-align:center;padding-top:50px}
.ev.mid{background:var(--card)}
.ev .day{font-size:22px;color:#7c7873}
.ev.mid .day{color:#a9a49f}
.ev .date{font-size:24px;margin:2px 0 12px}
.ev .time{font-size:12px;color:#8f8a85;margin-bottom:32px}
.ev p{font-size:11px;line-height:18px;color:#5e5a56}
.ev.mid p{color:#9a948e}
.arrow{top:2574px;width:74px;height:74px;border:1.5px solid #cfcac4;border-radius:50%}

/* newsletter */
.news-bg{left:0;top:2912px;width:1200px;height:480px;background:linear-gradient(100deg,#3b2a1d 0%,#7a5838 35%,#5c4129 60%,#3a2a1d 100%)}
.news-label{left:90px;top:2912px;width:487px;height:89px;background:#1a1918;font-size:56px;line-height:89px;padding-left:48px;color:#3f3d3b;font-weight:300}
.news-panel{left:578px;top:2853px;width:561px;height:539px;background:var(--tan);padding:60px 60px 0}
.news-panel h2{font-weight:400;font-size:24px;margin-bottom:18px}
.news-panel .lede{font-size:11.5px;line-height:18px;color:#f6ece2;margin-bottom:28px}
.field label{display:block;font-size:11.5px;margin-bottom:8px;color:#f6ece2}
.field .input{height:40px;background:#c09574;border:1px solid #c89e7c;border-radius:4px}
.row{display:flex;gap:8px;margin-bottom:24px}
.row .field{flex:1}
.subscribe{width:216px;height:40px;background:#d9b690;border-radius:4px;font-size:10px;text-transform:uppercase;text-align:center;line-height:40px;margin-top:20px}

/* footer */
.foot-panel{left:439px;top:3392px;width:334px;height:488px;background:#181716}
.foot-brand{left:439px;top:3460px;width:334px;text-align:center;font-weight:400;font-size:21px;letter-spacing:3px;line-height:1.4}
.foot-brand small{display:flex;align-items:center;justify-content:center;gap:12px;font-size:9px;letter-spacing:4px;margin-top:10px}
.foot-brand small i{display:block;width:38px;height:1px;background:var(--muted)}
.contact{left:439px;width:334px;text-align:center}
.contact .ic{width:20px;height:20px;border-radius:50%;background:var(--tan);margin:0 auto 10px}
.contact .lbl{font-size:10px;text-transform:uppercase;color:#d8d2cb;margin-bottom:4px}
.contact .val{font-size:12.5px;line-height:18px}
.foot-h{font-size:11px;color:var(--gold)}
.foot-nav{font-size:11px;line-height:17px;color:#8f6f55}
.social span{display:inline-block;width:13px;height:13px;border:1.5px solid #9a948e;border-radius:50%;margin-right:9px}
.copy{top:3909px;width:1200px;text-align:center;font-size:9.5px;color:#8f6f55;text-transform:uppercase}
</style>
</head>
<body>

<!-- hero -->
<section class="abs hero" role="img" aria-label="Photo of the historic sanctuary interior with arched stained windows and wooden pews"></section>
<nav class="abs nav" style="left:0;width:1200px">
  <span style="left:197px">Home</span>
  <span style="left:264px">About MF ⌄</span>
  <span style="left:373px">Ministries ⌄</span>
  <span style="left:758px">Bible Studies ⌄</span>
  <span style="left:876px">Sermon Library</span>
  <span style="left:999px">Donate</span>
</nav>
<div class="abs brand">MEADOWLARK<br>FELLOWSHIP<small>EST. 1928</small></div>
<div class="abs rail"></div>
<div class="abs dot" style="top:216px">01</div>
<div class="abs dot" style="top:246px">02</div>
<div class="abs dot" style="top:280px;width:30px;height:30px;left:46px;line-height:28px;border-color:#fff;color:#fff">03</div>
<div class="abs dot" style="top:320px">04</div>
<div class="abs dot" style="top:350px">05</div>
<h1 class="abs hero-title">Historic Church, Ancient Faith<br><span class="gold">Eternal Truth</span></h1>
<div class="abs watch"><div class="play"></div><span>Watch video</span><div class="rule"></div></div>
<div class="abs scroll">Scroll</div>

<!-- about -->
<div class="abs about-photo" role="img" aria-label="Photo of the white church building with a steeple beside a palm tree"></div>
<div class="abs vertical">ABOUT MF</div>
<h2 class="abs about-head">Meadowlark Fellowship is an <span class="gold">independent Christian church</span> in the Protestant tradition.</h2>
<p class="abs about-text">Its central tenets are found in its Articles of Faith and include belief in: the Deity and Lordship of Jesus Christ; the Trinity; Jesus' perfect life, atoning death on the cross, bodily resurrection, and ascension; Jesus' literal return; the inerrancy of the Bible in its original manuscripts; and our need for salvation through personal faith in Jesus Christ. In keeping with the prevailing perspective of the church during the centuries immediately following the Apostles, we teach Premillennialism. That is, the belief that Messiah will physically and literally return to earth at Jerusalem before the millennial age commences. At that time, he will establish a kingdom over which he will preside as King. All the promises of Israel's covenants will be literally fulfilled during this reign. At the end of one thousand years, the kingdom will be transferred from the Son to the Father (1 Cor 15:24-25) and it will merge with the eternal kingdom (Rev 20-21).</p>
<a class="abs btn-outline">Learn more</a>

<div class="abs pillar" style="left:241px">
  <svg width="40" height="44" viewBox="0 0 40 44" fill="none" stroke="#c9a27a" stroke-width="1.5"><path d="M20 2v14M14 7h12M8 22h24l-3 8H11zM4 34h32M8 40h24"/></svg>
  <div><h3>Our <span class="gold">mission</span></h3><p>MF exists to glorify the Triune God and make disciples of Jesus Christ.</p></div>
</div>
<div class="abs pillar" style="left:621px">
  <svg width="40" height="44" viewBox="0 0 40 44" fill="none" stroke="#c9a27a" stroke-width="1.5"><path d="M20 2v14M15 7h10M4 40l16-18 16 18M10 40l10-11 10 11M6 8l4 3M34 8l-4 3"/></svg>
  <div><h3>Our <span class="gold">purpose</span></h3><p>"To foster the promulgation of the fundamental doctrines of the Old and New Testaments, using all lawful means and avenues available."</p></div>
</div>

<!-- ministries -->
<div class="abs min-hall" role="img" aria-label="Photo of a grand library hall with columns and chandeliers"></div>
<div class="abs min-left" role="img" aria-label="Photo of an ornate vaulted library corridor"></div>
<div class="abs min-box">
  <h2>God has blessed <span style="color:#f0ddc8">Meadowlark Fellowship</span> with some very gifted people with hearts for service!</h2>
  <ul>
    <li>Small Groups &amp; Bible Studies<span>›</span></li>
    <li>Men's Ministry<span>›</span></li>
    <li>Women's Ministry<span>›</span></li>
    <li>Kids Church<span>›</span></li>
  </ul>
</div>
<div class="abs min-label">MF<br>MINISTRIES</div>

<!-- visit -->
<h2 class="abs sec-title" style="top:1936px">Visit us <span class="gold">this sunday!</span></h2>
<div class="abs visit">
  <div class="vl" style="left:0"></div>
  <div class="vl" style="left:329px"></div>
  <div class="vl" style="left:778px"></div>
  <div style="position:absolute;left:341px;top:137px;width:425px;height:1px;background:var(--line)"></div>
  <svg style="position:absolute;left:126px;top:18px" width="78" height="80" viewBox="0 0 78 80" fill="none" stroke="#8f8a85" stroke-width="2.5"><rect x="3" y="10" width="72" height="66" rx="6"/><path d="M3 28h72M22 3v14M56 3v14"/><g fill="#8f8a85" stroke="none"><circle cx="20" cy="42" r="3"/><circle cx="39" cy="42" r="3"/><circle cx="58" cy="42" r="3"/><circle cx="20" cy="60" r="3"/><circle cx="39" cy="60" r="3"/><circle cx="58" cy="60" r="3"/></g></svg>
  <div class="svc" style="left:0;width:329px;top:140px"><h3>Morning worship service</h3><div class="time">11:00 AM</div><p>Sunday morning worship and service<br>takes place in the main sanctuary.</p></div>
  <svg style="position:absolute;left:396px;top:42px" width="44" height="40" viewBox="0 0 44 40" fill="none" stroke="#6a6560" stroke-width="1.5"><path d="M22 2v12M17 6h10M6 18h32l-3 8H9zM2 30h40M8 36h28"/></svg>
  <div class="svc" style="left:341px;width:437px;top:4px"><h3>All church lunch</h3><div class="time">12:15 PM</div><p>• Family Room •<br>Please join us for lunch after the service.<br>Everyone is welcome!</p></div>
  <svg style="position:absolute;left:396px;top:195px" width="44" height="36" viewBox="0 0 44 36" fill="none" stroke="#6a6560" stroke-width="1.5"><path d="M4 6h16l2 4 2-4h16v24H24l-2 4-2-4H4zM22 10v20"/></svg>
  <div class="svc" style="left:341px;width:437px;top:163px"><h3>Afternoon adult bible study</h3><div class="time">12:45 PM</div><p>• Patio Room •<br>TBA</p></div>
</div>

<!-- events -->
<h2 class="abs sec-title" style="top:2401px">Upcoming <span class="gold">events</span></h2>
<div class="abs arrow" style="left:59px"><svg width="74" height="74" viewBox="0 0 74 74" fill="none" stroke="#fff" stroke-width="2"><path d="M40 30l-7 7 7 7"/></svg></div>
<div class="abs ev" style="left:181px"><div class="day">Wed</div><div class="date">Jan 20, 2026</div><div class="time">7:30 PM</div><p>Wednesday night<br>bible study</p></div>
<div class="abs ev mid" style="left:470px"><div class="day">Sun</div><div class="date">Jan 25, 2026</div><div class="time">11:00 AM</div><p>Sunday service</p></div>
<div class="abs ev" style="left:762px"><div class="day">Wed</div><div class="date">Jan 28, 2026</div><div class="time">7:30 PM</div><p>Wednesday night<br>bible study</p></div>
<div class="abs arrow" style="left:1067px"><svg width="74" height="74" viewBox="0 0 74 74" fill="none" stroke="#fff" stroke-width="2"><path d="M34 30l7 7-7 7"/></svg></div>

<!-- newsletter -->
<div class="abs news-bg" role="img" aria-label="Photo of an antique map with a pocket watch and compass"></div>
<div class="abs news-label">NEWSLETTER</div>
<form class="abs news-panel">
  <h2>Sign up for our weekly newsletter</h2>
  <p class="lede">Lorem ipsum dolor sit amet, consectetur adipiscing elit, sed do eiusmod tempor incididunt ut labore et dolore magna aliqua. Ut enim ad minim ve niam, quis nostrud exercitation ullamco laboris nisi ut aliquip ex ea comm odo consequat.</p>
  <div class="row">
    <div class="field"><label>First Name</label><div class="input"></div></div>
    <div class="field"><label>Last Name</label><div class="input"></div></div>
  </div>
  <div class="field"><label>Email</label><div class="input"></div></div>
  <div class="subscribe">Subscribe</div>
</form>

<!-- footer -->
<div class="abs foot-panel"></div>
<div class="abs foot-brand">MEADOWLARK<br>FELLOWSHIP<small><i></i>EST. 1928<i></i></small></div>
<div class="abs contact" style="top:3590px"><div class="ic"></div><div class="lbl">Call us</div><div class="val">555.204.3187</div></div>
<div class="abs contact" style="top:3674px"><div class="ic"></div><div class="lbl">Email us</div><div class="val">info@meadowlarkfellowship.org</div></div>
<div class="abs contact" style="top:3758px"><div class="ic"></div><div class="lbl">Visit us</div><div class="val">2240 Alder Row<br>Pasadena, California 91101</div></div>
<div class="abs foot-h" style="left:210px;top:3532px">Navigation</div>
<div class="abs foot-nav" style="left:210px;top:3566px">Home<br>About MF<br>Ministries<br>Bible Studies<br>Sermon Library<br>Donate</div>
<div class="abs foot-h" style="left:865px;top:3532px">Connect with us</div>
<div class="abs social" style="left:865px;top:3565px"><span></span><span></span><span></span><span></span></div>
<div class="abs copy">Copyright © 2026 Meadowlark Fellowship. All rights reserved</div>

</body>
</html>
```